Rack card for marketing

Office to office marketing for knee pain treatment

Target Market(s)

Medical Offices, Retired patients looking to maintain active lifestlye. Family practice medical offices

Industry/Entity Type

Medical

Colors
0054AA
0677BA
7BADD7
CADEEF
E8F1F8

Requirements
Must have
• Font that matches logo, GRM logo, graphic of a retiree who looks active and happy versus a knee graphic
Nice to have
• The best ever rack card!!! Easy to Read, simplicity is key.

```html
<!DOCTYPE html>
<html lang="en">
<head>
<meta charset="utf-8">
<title>GRM Knee Pain Rack Card</title>
<link href="https://fonts.googleapis.com/css2?family=Playfair+Display:wght@900&family=Domine:wght@500;700&family=Poppins:wght@400;600&display=swap" rel="stylesheet">
<style>
  :root {
    --ink: #333333;
    --text-grey: #6b6b6b;
    --sky: #0a8bd6;
    --sky-light: #3fbcd8;
    --deep: #0054aa;
    --mid: #0677ba;
    --footer: #0591d8;
    --mist: #f4f4f4;
    --logo-blue: #25567a;
    --logo-grey: #8a8a8a;
    --white: #ffffff;
  }
  * { margin: 0; padding: 0; box-sizing: border-box; }
  html, body { width: 852px; height: 1200px; overflow: hidden; background: var(--white); }
  .card { position: relative; width: 852px; height: 1200px; overflow: hidden; background: var(--white); font-family: "Domine", serif; }
  .shapes { position: absolute; inset: 0; }
  .brand { position: absolute; left: 598px; top: 34px; }
  .brand-name { font-family: "Domine", serif; font-weight: 700; font-size: 43px; line-height: 1; color: var(--logo-blue); letter-spacing: 1px; }
  .brand-sub { font-family: "Domine", serif; font-weight: 700; font-size: 17px; color: var(--logo-blue); margin-top: 6px; }
  .headline { position: absolute; right: 34px; top: 292px; text-align: right; font-family: "Playfair Display", serif; font-weight: 900; font-size: 66px; line-height: 71px; letter-spacing: -2.5px; }
  .headline .dark { color: var(--ink); display: block; }
  .headline .blue { color: var(--sky); display: block; }
  .rule { position: absolute; left: 734px; top: 594px; width: 84px; height: 4px; background: var(--sky); }
  .col { position: absolute; top: 625px; }
  .col-left { left: 306px; width: 280px; }
  .col-right { left: 601px; width: 230px; }
  .col h2 { font-family: "Domine", serif; font-weight: 700; font-size: 21px; line-height: 27.5px; color: var(--sky); text-transform: uppercase; margin-bottom: 6px; }
  .col ul { list-style: none; }
  .col li { font-weight: 700; font-size: 13.6px; line-height: 25.6px; color: var(--text-grey); padding-left: 13px; position: relative; white-space: nowrap; }
  .col li::before { content: "–"; position: absolute; left: 0; font-weight: 500; }
  .col li.sub { padding-left: 25px; }
  .col li.sub::before { content: "◦"; left: 11px; }
  .col-right li { font-size: 13.2px; white-space: normal; }
  .web { position: absolute; left: 98px; top: 1133px; font-family: "Poppins", sans-serif; font-size: 23px; color: var(--white); }
  .call { position: absolute; left: 568px; top: 1108px; font-family: "Poppins", sans-serif; color: var(--white); }
  .call-label { font-size: 20.5px; line-height: 26px; color: var(--ink); opacity: .85; }
  .call-number { font-size: 27px; line-height: 34px; font-weight: 600; }
</style>
</head>
<body>
<div class="card">
  <svg class="shapes" width="852" height="1200" viewBox="0 0 852 1200">
    <defs>
      <linearGradient id="sideBlue" x1="0" y1="0" x2="1" y2="0">
        <stop offset="0" stop-color="#3fbcd8"/>
        <stop offset="1" stop-color="#2a7fc4"/>
      </linearGradient>
      <linearGradient id="photoTone" x1="0" y1="0" x2="1" y2="1">
        <stop offset="0" stop-color="#c79a3c"/>
        <stop offset=".5" stop-color="#8a6a44"/>
        <stop offset="1" stop-color="#3e6a7a"/>
      </linearGradient>
      <linearGradient id="callBox" x1="0" y1="0" x2="1" y2="0">
        <stop offset="0" stop-color="#35b7dc"/>
        <stop offset="1" stop-color="#1f7cc4"/>
      </linearGradient>
    </defs>
    <polygon points="481,0 852,0 852,153 566,153" fill="var(--mist)"/>
    <polygon points="0,545 342,545 61,1032 0,1032" fill="var(--mist)"/>
    <polygon points="0,545 285,545 61,935 0,935" fill="url(#sideBlue)"/>
    <polygon points="0,0 481,0 566,153 342,545 0,545" fill="url(#photoTone)" role="img" aria-label="Photo: active grandparents swinging a smiling granddaughter between them on an autumn park walk"/>
    <rect x="0" y="1111" width="483" height="89" fill="var(--footer)"/>
    <polygon points="455,1111 483,1074 483,1111" fill="#1f7cc4"/>
    <rect x="483" y="1074" width="369" height="126" fill="url(#callBox)"/>
    <circle cx="68" cy="1150" r="18" fill="var(--white)"/>
    <g fill="none" stroke="var(--footer)" stroke-width="3" stroke-linecap="round">
      <path d="M63,1155 l-3,3 a4,4 0 0 1 -6,-6 l5,-5 a4,4 0 0 1 6,0"/>
      <path d="M73,1145 l3,-3 a4,4 0 0 1 6,6 l-5,5 a4,4 0 0 1 -6,0"/>
      <line x1="64" y1="1154" x2="72" y2="1146"/>
    </g>
    <rect x="514" y="1119" width="7" height="46" fill="var(--white)"/>
    <rect x="525" y="1119" width="33" height="46" fill="var(--white)"/>
    <path d="M533,1130 c2,-2 4,-1 5,1 l2,4 c0,2 -2,2 -2,3 c1,3 4,6 7,7 c1,0 1,-2 3,-2 l4,2 c2,1 3,3 1,5 c-6,5 -22,-9 -20,-20z" fill="var(--footer)"/>
  </svg>

  <div class="brand">
    <div class="brand-name">GRM</div>
    <div class="brand-sub">Gulf Ridge Medical</div>
  </div>

  <h1 class="headline">
    <span class="dark">KNEE PAIN</span>
    <span class="dark">PROBLEMS?</span>
    <span class="blue">TIME TO SAY</span>
    <span class="blue">GOOD BYE</span>
  </h1>
  <div class="rule"></div>

  <section class="col col-left">
    <h2>Comprehensive<br>Non-Operative<br>Treatment for<br>Knee Pain</h2>
    <ul>
      <li>Nonsurgical Options</li>
      <li>Customized Bracing</li>
      <li>Topical Medications</li>
      <li>Topical Supplements</li>
      <li>Evidence Based Supplementation</li>
      <li>Cryotherapy / Cold Compression</li>
      <li>Acupuncture / Electrical Therapy</li>
      <li>Exercise Protocols</li>
      <li class="sub">Athletic Trainer</li>
      <li class="sub">Exercise Physiologist</li>
      <li class="sub">Home based exercise options</li>
    </ul>
  </section>

  <section class="col col-right">
    <h2>Procedures<br>Offered:</h2>
    <ul>
      <li>Interarticular Knee Injection</li>
      <li>Pes Anserine Bursa</li>
      <li>Genicular Nerve Block</li>
      <li>Genicular Radiofrequency Ablation</li>
      <li>HA (hyaluronic acid) Injections</li>
      <li>Arnivex Injections</li>
    </ul>
  </section>

  <div class="web">www.gulfridgemed.com</div>
  <div class="call">
    <div class="call-label">Call for more info</div>
    <div class="call-number">+1 555 014 0979</div>
  </div>
</div>
</body>
</html>
```